Web Design Project - Dating and Social Networking Site for Artists

Hello,
Need a homepage design for Quillory.net, an existing dating and networking site for artists. The theme for this site is: "Find or serve as a Muse." Greek God and Goddess (Muse) theme is welcome, but not required. Website is geared toward 20 - 45 year old individuals. Existing background colors are blue, green and white. Nothing too slick, cheesy or serious. The final design should communicate uniqueness, romance and excitement. Playful is good too!
Industry/Entity Type
Dating
Look and feel

```html
<!DOCTYPE html>
<html lang="en">
<head>
<meta charset="utf-8">
<title>Quillory.net – Where heart and art meet</title>
<link rel="stylesheet" href="https://fonts.googleapis.com/css2?family=Quicksand:wght@400;500;600;700&display=swap">
<style>
:root{
  --green:#007b48;
  --blue:#0a9bcc;
  --white:#ffffff;
  --khaki:#d6c76e;
  --ink:#0f4d3a;
  --grey:#555555;
  --tan:#b9a574;
  --pink:#e8477d;
  --statue:#c9c9c9;
}
*{margin:0;padding:0;box-sizing:border-box}
html,body{width:1200px;height:657px;overflow:hidden}
body{
  font-family:"Quicksand",sans-serif;
  background:repeating-linear-gradient(180deg,var(--green) 0 17.5px,var(--blue) 17.5px 35px);
  position:relative;
}
.page{
  position:absolute;left:27px;top:24px;width:1145px;height:608px;
  background:var(--white);border-radius:20px;
}
.brand{
  position:absolute;left:218px;top:30px;width:410px;height:100px;
  display:flex;flex-direction:column;align-items:center;justify-content:center;
}
.brand-name{font-size:50px;font-weight:700;color:var(--green);letter-spacing:1px;line-height:1}
.brand-line{font-size:15px;font-weight:600;color:var(--green);margin-top:6px}
.login{
  position:absolute;left:725px;top:22px;width:251px;height:72px;
  background:var(--blue);border-radius:10px;padding:2px 26px;
  text-align:center;font-weight:700;font-size:15px;color:#143a4a;
}
.login label{display:block;line-height:17px}
.login .field{display:block;height:14px;background:var(--white);border-radius:2px;margin-bottom:2px}
.create{
  position:absolute;left:725px;top:102px;width:251px;height:36px;
  background:var(--green);border-radius:10px;color:var(--white);
  font-weight:700;font-size:15px;display:flex;align-items:center;justify-content:center;
}
.nav{
  position:absolute;left:164px;top:188px;width:818px;height:35px;
  background:var(--khaki);border-radius:4px;
  display:flex;align-items:center;justify-content:center;
  font-size:22px;font-weight:500;color:var(--ink);
}
.nav span{padding:0 5px;border-right:2px solid var(--blue);line-height:22px}
.nav span:last-child{border-right:none}
.statue{position:absolute;top:199px;width:163px;height:278px;
  background:linear-gradient(180deg,#e4e4e4,var(--statue));border-radius:40px 40px 4px 4px}
.statue.left{left:6px}
.statue.right{left:976px}
.intro{
  position:absolute;left:169px;top:263px;width:490px;text-align:center;
  font-size:12px;line-height:15px;color:var(--grey);
}
.intro p{margin-bottom:13px}
.intro .quote{font-weight:700;font-style:italic;color:#222;font-size:12.5px}
.members{
  position:absolute;left:689px;top:265px;width:273px;height:207px;
  border:2px solid var(--tan);border-radius:9px;background:#f7f6f0;
}
.tabs{height:22px;background:#e8e0b8;border-radius:7px 7px 0 0;display:flex;
  align-items:center;justify-content:center;font-size:13px}
.tabs .on{font-weight:700;color:#222;padding-right:9px;border-right:2px solid var(--blue)}
.tabs .off{color:#7a6d3a;padding-left:9px}
.grid{display:grid;grid-template-columns:repeat(6,36px);gap:8px 7px;padding:8px 9px}
.grid i{width:36px;height:36px;border:2px solid var(--blue);border-radius:2px;display:block}
.c1{background:linear-gradient(#f08a3a,#3a4a8a)}
.c2{background:linear-gradient(#555,#222)}
.c3{background:linear-gradient(#444,#111)}
.c4{background:linear-gradient(#e4b040,#b06030)}
.c5{background:linear-gradient(#c09050,#604020)}
.c6{background:linear-gradient(#f3c8a8,#c05040)}
.footer{position:absolute;left:0;top:537px;width:1145px;text-align:center;
  font-size:7px;color:var(--grey);text-transform:uppercase;line-height:9px}
.footer .offer{color:var(--pink);font-weight:700}
.footer .pink{color:var(--pink);text-transform:none}
.footer b{color:#222}
.footer .contact{margin-top:13px}
</style>
</head>
<body>
<div class="page">
  <div class="brand">
    <div class="brand-name">Quillory.net</div>
    <div class="brand-line">Where heart &amp; art connect… Since forever.</div>
  </div>

  <form class="login">
    <label>Username or email</label><span class="field"></span>
    <label>Password</label><span class="field"></span>
  </form>
  <div class="create">CREATE NEW PROFILE</div>

  <nav class="nav">
    <span>Home</span><span>News</span><span>Sign up</span><span>Search</span><span>Blogs</span><span>Pictures</span><span>Videos</span><span>Events</span><span>Hot or Not</span>
  </nav>

  <div class="statue left" role="img" aria-label="Engraved statue of a muse playing a double flute"></div>
  <div class="statue right" role="img" aria-label="Engraved statue of a muse playing a double flute"></div>

  <div class="intro">
    <p>Where heart and art meet….since forever. The dating and networking site for the creative. Single and seeking? Looking to connect with other artists? This is the place for you!</p>
    <p>Musicians, painters, writers, actors, sculptors, photographers, poets, performance artists, cartoonists, actresses, singers, comics, artisens and more all meet up here.</p>
    <p>Sometimes a spark is needed to be given or received. Ask Varnell, or Ostrova, or Delacquer. Discover, colloborate, share your passion, make a connection. Find true love or friendship. Find or be a creative inspiration.</p>
    <p>Muses, Graces and Fates await you here….create a profile today!</p>
    <p class="quote">"An artist cannot fail; it is a success to be one." ~Edwin Harlow Pryce~</p>
  </div>

  <div class="members">
    <div class="tabs"><span class="on">Popular members</span><span class="off">New members</span></div>
    <div class="grid" role="img" aria-label="Grid of member profile photos">
      <i class="c1"></i><i class="c2"></i><i class="c3"></i><i class="c4"></i><i class="c5"></i><i class="c6"></i>
      <i class="c1"></i><i class="c2"></i><i class="c3"></i><i class="c4"></i><i class="c5"></i><i class="c6"></i>
      <i class="c1"></i><i class="c2"></i><i class="c3"></i><i class="c4"></i><i class="c5"></i><i class="c6"></i>
      <i class="c1"></i><i class="c2"></i><i class="c3"></i><i class="c4"></i><i class="c5"></i><i class="c6"></i>
    </div>
  </div>

  <footer class="footer">
    <div class="offer">Limited time offer! Free</div>
    <div><span class="pink">1 Month Membership!</span> - Communicate with other members by messages, gifts, and comments - Share pictures, music, videos, and blogs - Create &amp; join events and much more <b>Starting as low as $9.99 per month!</b></div>
    <div class="contact">Questions? Contact us at service@quillory.net</div>
  </footer>
</div>
</body>
</html>
```